Lanterns of the Silent Vale - Islamic Book about death, grave and the hereafter

We need a complete redesign of an old book cover. It is a book about death, the grave, the day of judgment, hellfire and paradise. i've attached our old bookcover. you can take new colors and change completly the design. It is up to you!

```html
<!DOCTYPE html>
<html lang="de">
<head>
<meta charset="utf-8">
<title>Lanterns of the Silent Vale – Cover Concepts</title>
<link rel="stylesheet" href="https://fonts.googleapis.com/css2?family=Quicksand:wght@500;700&family=Archivo+Black&family=Roboto+Condensed:wght@700&display=swap">
<style>
  :root {
    --paper: #ffffff;
    --ink: #111111;
    --cover-text: #ffffff;
    --outline: #000000;
    --dome-light: #f0c9a0;
    --dome-mid: #c98a55;
    --dome-dark: #4a2a18;
    --sky-light: #cfe3ea;
    --sky-blue: #2f6fb0;
    --sky-deep: #12335f;
    --night: #050507;
    --flame-deep: #7a1a05;
    --flame: #e2561a;
    --flame-bright: #ffb13b;
  }
  * { box-sizing: border-box; margin: 0; padding: 0; }
  html, body { width: 1200px; height: 1200px; overflow: hidden; background: var(--paper); }
  .board { position: relative; width: 1200px; height: 1200px; background: var(--paper); }

  .cover { position: absolute; top: 25px; height: 893px; overflow: hidden; }
  .cover--dome { left: 0; width: 605px; }
  .cover--fire { left: 607px; width: 593px; }

  .cover__art { position: absolute; inset: 0; width: 100%; height: 100%; display: block; }

  .cover__text {
    position: absolute; left: 0; right: 0; text-align: center;
    color: var(--cover-text);
    font-family: "Quicksand", sans-serif; font-weight: 700; text-transform: uppercase;
    text-shadow: -2px -2px 0 var(--outline), 2px -2px 0 var(--outline),
                 -2px 2px 0 var(--outline), 2px 2px 0 var(--outline);
  }
  .cover__author { top: 105px; font-size: 38px; line-height: 38px; letter-spacing: -1px; }
  .cover__title { top: 318px; font-size: 70px; line-height: 68px; letter-spacing: -1px; }
  .cover__subtitle { top: 678px; font-size: 24px; line-height: 24px; font-style: italic; letter-spacing: -1px; }
  .cover__publisher { top: 826px; font-size: 27px; line-height: 27px; letter-spacing: -1px; }

  .caption { position: absolute; left: 20px; top: 940px; right: 20px; color: var(--ink); }
  .caption__heading { font-family: "Archivo Black", sans-serif; font-size: 29px; line-height: 40px; }
  .caption__body {
    margin-top: 2px;
    font-family: "Roboto Condensed", sans-serif; font-weight: 700;
    font-size: 29px; line-height: 43.5px; letter-spacing: -0.3px;
  }
</style>
</head>
<body>
<main class="board">

  <section class="cover cover--dome">
    <svg class="cover__art" role="img" aria-label="Photograph looking up into an ornate mosque dome with painted arches and windows" viewBox="0 0 605 893" preserveAspectRatio="none">
      <defs>
        <radialGradient id="domeGlow" cx="50%" cy="48%" r="70%">
          <stop offset="0" stop-color="var(--dome-light)"/>
          <stop offset="0.55" stop-color="var(--dome-mid)"/>
          <stop offset="1" stop-color="var(--dome-dark)"/>
        </radialGradient>
      </defs>
      <rect width="605" height="893" fill="url(#domeGlow)"/>
    </svg>
    <p class="cover__text cover__author">Samira<br>Haddad-Noor</p>
    <h1 class="cover__text cover__title">Lanterns<br>of the<br>Silent<br>Vale</h1>
    <p class="cover__text cover__subtitle">Über den Tod und das Leben<br>danach</p>
    <p class="cover__text cover__publisher">Helle Pforte Verlag</p>
  </section>

  <section class="cover cover--fire">
    <svg class="cover__art" role="img" aria-label="Photograph of a dramatic blue cloudy sky over dark water, with flames rising from below" viewBox="0 0 593 893" preserveAspectRatio="none">
      <defs>
        <linearGradient id="skyToFire" x1="0" y1="0" x2="0" y2="1">
          <stop offset="0" stop-color="var(--sky-deep)"/>
          <stop offset="0.14" stop-color="var(--sky-blue)"/>
          <stop offset="0.24" stop-color="var(--sky-light)"/>
          <stop offset="0.3" stop-color="var(--sky-blue)"/>
          <stop offset="0.4" stop-color="var(--night)"/>
          <stop offset="0.5" stop-color="var(--night)"/>
          <stop offset="0.62" stop-color="var(--flame-deep)"/>
          <stop offset="0.8" stop-color="var(--flame)"/>
          <stop offset="1" stop-color="var(--flame-bright)"/>
        </linearGradient>
      </defs>
      <rect width="593" height="893" fill="url(#skyToFire)"/>
    </svg>
    <p class="cover__text cover__author">Samira<br>Haddad-Noor</p>
    <h1 class="cover__text cover__title">Lanterns<br>of the<br>Silent<br>Vale</h1>
    <p class="cover__text cover__subtitle">Über den Tod und das Leben<br>danach</p>
    <p class="cover__text cover__publisher">Helle Pforte Verlag</p>
  </section>

  <section class="caption">
    <h2 class="caption__heading">Islamic book designs</h2>
    <p class="caption__body">Only submitting the front pages for now. I went for modern designs which is becoming popular with islamic books and also with contemporary. If neither is preferred then let me know what you would like to see! If any of the following designs are preferred then let me know so I can show you the back and spine of book.</p>
  </section>

</main>
</body>
</html>
```